We need a book cover design for a handbook related to the implementation of new European privacy regulation. The topic is quite technical but the goal is to have something actionnable for small businesses and small non-profit organizations. It's really a handbook that should inspire confidence for the managers who have to be compliant in a pragmatic way (not like big corporate structures). The final format should be in PDF with specific requirements to be publish on PrintHollow.com.

Title: KVRT Guidebook for local traders
Subtitle: Be ready in 21 days (or less)
Author: Marcel Vendrione
Edition: 1.0
ISBN-13: 978-1574203658
ISBN-10: 1574203652

The book has a size of 6" x 9" and is composed by 52 pages.
Spine width should be 52 x 0.002252 = 0,117104"
Additional technical info in the attachments.

For text and inspiration about the covers (rear cover especially), please use the text on https://www.kvrt-guidebook.eu.

Feel free to ask questions to clarify some aspects!

Target Market(s)

Managing Directors of small businesses

Industry/Entity Type

Technical

Colors

Designer to choose colors to be used in the design.

Requirements
Must have
• - Inspire confidence and accessibility (simple, easy, time effective)
• - Title, subtitle and author on the front cover
• - ISBNs, barcode and mention "Templates available on https://www.kvrt-guidebook.eu" + text coming from the website
Nice to have
• - Simplicity
• - Easy path to compliance, shortcut
• - Time saving
Should not have
• - Picture of the author
• - Text on the spine

```html
<!DOCTYPE html>
<html lang="en">
<head>
<meta charset="utf-8">
<title>KVRT Guidebook for local traders — Front Cover</title>
<link rel="stylesheet" href="https://fonts.googleapis.com/css2?family=Anton&family=Montserrat:wght@400;500&display=swap">
<style>
  :root {
    --board: #2e2e2f;
    --board-edge: #262627;
    --chalk: #ececec;
    --chalk-soft: #d4d4d4;
    --accent: #d9c61c;
    --accent-deep: #b8a514;
  }
  html, body {
    margin: 0;
    padding: 0;
    width: 1017px;
    height: 1200px;
    overflow: hidden;
    background: var(--board);
  }
  .cover {
    position: relative;
    width: 1017px;
    height: 1200px;
    background: radial-gradient(ellipse at 45% 40%, #363637 0%, var(--board) 55%, var(--board-edge) 100%);
    overflow: hidden;
  }
  .stars {
    position: absolute;
    inset: 0;
    width: 1017px;
    height: 1200px;
  }
  .stars polygon { fill: var(--accent); }
  .title {
    position: absolute;
    left: 96px;
    top: 200px;
    margin: 0;
    font-family: "Anton", "Oswald", sans-serif;
    font-weight: 400;
    font-size: 80px;
    line-height: 1.08;
    color: var(--chalk);
    letter-spacing: -0.5px;
  }
  .title span { display: block; }
  .title-rule {
    position: absolute;
    left: 100px;
    top: 426px;
    width: 294px;
    height: 4px;
    background: var(--accent);
  }
  .subtitle {
    position: absolute;
    left: 100px;
    top: 466px;
    margin: 0;
    font-family: "Montserrat", sans-serif;
    font-weight: 500;
    font-size: 36px;
    color: var(--chalk);
  }
  .illustration {
    position: absolute;
    left: 62px;
    top: 700px;
    width: 913px;
    height: 322px;
    border-radius: 6px;
    background:
      radial-gradient(ellipse 160px 150px at 38% 50%, var(--accent) 0%, var(--accent-deep) 55%, transparent 80%),
      linear-gradient(90deg, rgba(220,220,220,0.18) 0%, rgba(220,220,220,0.08) 35%, transparent 45%, rgba(220,220,220,0.12) 60%, rgba(220,220,220,0.18) 100%);
  }
  .author {
    position: absolute;
    left: 0;
    right: 0;
    top: 1098px;
    margin: 0;
    text-align: center;
    font-family: "Montserrat", sans-serif;
    font-weight: 400;
    font-size: 28px;
    letter-spacing: 0.55em;
    color: var(--chalk-soft);
    text-transform: uppercase;
  }
</style>
</head>
<body>
  <main class="cover">
    <svg class="stars" viewBox="0 0 1017 1200" aria-hidden="true">
      <defs>
        <polygon id="star" points="0,-30 7,-9.5 28.5,-9.3 11.3,3.6 17.6,24.3 0,11.8 -17.6,24.3 -11.3,3.6 -28.5,-9.3 -7,-9.5"/>
      </defs>
      <use href="#star" x="712" y="62"/>
      <use href="#star" x="762" y="168"/>
      <use href="#star" x="880" y="226"/>
    </svg>

    <h1 class="title">
      <span>KVRT Guidebook</span>
      <span>for local traders</span>
    </h1>
    <div class="title-rule"></div>
    <p class="subtitle">Be ready in 21 days (or less)</p>

    <div class="illustration" role="img" aria-label="Chalk illustration: tangled white lines passing through a yellow padlock and leaving as straight parallel arrows"></div>

    <p class="author">Marcel Vendrione</p>
  </main>
</body>
</html>
```